Wein- und Esswarenetiketten gesucht
Zielgruppe
Handel mit Getränken und Esswaren aus Italien.
Zielgruppe primär Privatpersonen, aber auch b2b (Gastronomie)
Neu möchten wir eigene Produktlinie(n) aufbauen: Rot- und Weisswein, aber auch Pasta, ...
Aufgabenstellung
Entwickeln eines einheitlichen Auftritts via Produktetiketten. Wein- und Esswarenetiketten sollen alle deutlich erkennbar sein, dasselbe Layout, denselben spirit ... zeigen. Der Kunde soll bei allen Produkten sofort an uns denken.
Bei Weinetiketten frei gestaltbar, da gesetzl. Angaben jeweils bereits auf Rückseite der Flaschen. Bei den Esswarenetiketten ev. Platz für Zusatzangaben ('Nutrifacts') zusätzlich vorsehen.
Design eher ruhig, klassisch, nicht zu verspielt. Ev. auch fast nur Worte/Text?
Keine Bilder, eher nur 'Symbole'

```html
<!DOCTYPE html>
<html lang="de">
<head>
<meta charset="utf-8">
<title>Tanto Sole – Produktetiketten</title>
<link rel="stylesheet" href="https://fonts.googleapis.com/css2?family=Crimson+Text:wght@400;700&family=Roboto+Condensed:wght@400&display=swap">
<style>
  :root {
    --bg: #e2e2e2;
    --label: #ffffff;
    --ink: #111111;
    --pasta-green: #a8cc00;
    --wine-red: #cc0000;
    --wine-ink: #2a0a0a;
    --sketch-dark: #6a6a6a;
    --sketch-light: #d8d8d8;
    --serif: "Crimson Text", "Times New Roman", serif;
    --sans: "Roboto Condensed", "Arial Narrow", sans-serif;
  }
  * { box-sizing: border-box; margin: 0; padding: 0; }
  html, body { width: 1139px; height: 1200px; overflow: hidden; }
  body { background: var(--bg); position: relative; color: var(--ink); }

  .label {
    position: absolute;
    background: var(--label);
    box-shadow: 0 2px 8px rgba(0,0,0,0.12);
    text-align: center;
  }
  .label--pasta { border-radius: 14px; overflow: hidden; }
  .label--spaghetti { left: 73px; top: 383px; width: 197px; height: 381px; }
  .label--fusilli { left: 389px; top: 572px; width: 327px; height: 295px; }
  .label--wine { left: 882px; top: 515px; width: 205px; height: 307px; }

  .label > * { position: absolute; left: 0; right: 0; }

  .brand { font-family: var(--serif); font-weight: 400; }
  .brand__name {
    font-size: 17px; letter-spacing: 1px; text-transform: uppercase; line-height: 1;
  }
  .brand__tagline { font-size: 11px; line-height: 1; }

  .claim { font-family: var(--sans); font-size: 11px; line-height: 14px; }

  .band { display: flex; flex-direction: column; align-items: center; justify-content: center; }
  .band--pasta { background: var(--pasta-green); top: 141px; height: 62px; }
  .band--wine { background: var(--wine-red); top: 86px; height: 63px; }

  .product-name { font-family: var(--serif); font-weight: 700; font-size: 22px; line-height: 1; letter-spacing: 0.5px; }
  .quality { font-family: var(--sans); font-size: 11px; margin-top: 5px; }
  .wine-name { font-family: var(--serif); font-weight: 400; font-size: 23px; line-height: 25px; color: var(--wine-ink); }

  .wine-facts { font-family: var(--sans); font-size: 11px; line-height: 14px; text-transform: uppercase; top: 152px; }

  .sketch {
    left: auto; right: auto;
    background: linear-gradient(90deg, var(--sketch-dark), var(--sketch-light));
    opacity: 0.55;
  }
  .sketch--wheat { height: 30px; border-radius: 50%; }
  .sketch--grapes { background: linear-gradient(180deg, var(--sketch-light), var(--sketch-dark)); border-radius: 40% 40% 50% 50%; }

  .quantity { font-family: var(--sans); font-size: 20px; line-height: 1; }
</style>
</head>
<body>

  <section class="label label--pasta label--spaghetti">
    <div class="brand" style="top:34px">
      <p class="brand__name">Tanto Sole</p>
      <p class="brand__tagline" style="margin-top:4px">sapori del sud</p>
    </div>
    <p class="claim" style="top:104px">Original italienische Nudeln<br>aus Hartweizengrieß</p>
    <div class="band band--pasta">
      <p class="product-name">SPAGHETTI</p>
      <p class="quality">Premium-Qualität</p>
    </div>
    <div class="sketch sketch--wheat" role="img" aria-label="Zeichnung zweier Weizenähren" style="left:49px; width:110px; top:212px"></div>
    <p class="quantity" style="top:334px">500g</p>
  </section>

  <section class="label label--pasta label--fusilli">
    <div class="brand" style="top:36px">
      <p class="brand__name">Tanto Sole</p>
      <p class="brand__tagline" style="margin-top:4px">sapori del sud</p>
    </div>
    <p class="claim" style="top:104px">Original italienische Nudeln<br>aus Hartweizengrieß</p>
    <div class="band band--pasta">
      <p class="product-name">FUSSILI</p>
      <p class="quality">Premium-Qualität</p>
    </div>
    <div class="sketch sketch--wheat" role="img" aria-label="Zeichnung zweier Weizenähren" style="left:109px; width:112px; top:212px"></div>
    <p class="quantity" style="top:258px">500g</p>
  </section>

  <section class="label label--wine">
    <div class="brand" style="top:24px">
      <p class="brand__name">Tanto Sole</p>
      <p class="brand__tagline" style="margin-top:4px">sapori del sud</p>
    </div>
    <div class="band band--wine">
      <p class="wine-name">MERLOT<br>2018</p>
    </div>
    <p class="wine-facts">Trocken<br>Original<br>aus der Toscana</p>
    <div class="sketch sketch--grapes" role="img" aria-label="Zeichnung einer Weintraube mit Blättern" style="left:77px; width:55px; top:197px; height:70px"></div>
    <p class="quantity" style="top:281px">0,7 l</p>
  </section>

</body>
</html>
```